Fernvale Craft Works business card design- Fine Art sculpture business (Contract guaranteed)

This business card is for a fine art business. Though we don't have a website up and running yet it should be up soon. I would like the business card to be elegant and fairly simple with a picture of one of my sculptures on the front (you might need to photoshop out the background) as well as my basic contact info (my name,phone # and e-mail). On the back I'd like it to be pretty simple with just "Notes" and some blank lines for writing in info.

Target Market(s)

High end artwork buyers

Industry/Entity Type

Art Gallery

Contact Information for Business Card

Marlo Prewitt Phone: (555) 213-4098 E-mail: marlo@quillbrookmail.com Facebook: @fernvalecraftworks Instagram: fernvalecraftworks

Colors

Designer to choose colors to be used in the design.

Requirements
Must have
• *A picture of one of my sculptures*, my name, business name (Fernvale Craft Works), e-mail, phone #, and a notes section on the back.
• Fernvale Craft Works
• Marlo Prewitt
• (555)213-4098
• marlo@quillbrookmail.com
• Facebook: @fernvalecraftworks
• Instagram: fernvalecraftworks
Nice to have
• It'd be nice if you can crop out the background in the sculpture pictures, which ever one you end up using.

```html
<!DOCTYPE html>
<html lang="en">
<head>
<meta charset="utf-8">
<title>Fernvale Craft Works – Business Card</title>
<link href="https://fonts.googleapis.com/css2?family=Montserrat:wght@400;700&display=swap" rel="stylesheet">
<style>
  :root {
    --page: #ffffff;
    --ink: #1f1f1f;
    --frame-front: #2b2b2b;
    --frame-back: #9a9a9a;
    --stone-dark: #4a3f3b;
    --stone-mid: #6e625d;
    --stone-light: #9b908b;
    --stone-pale-a: #d8d1ce;
    --stone-pale-b: #b9aea8;
    --rule: #cfc8c4;
  }
  html, body {
    margin: 0;
    padding: 0;
    width: 992px;
    height: 1200px;
    overflow: hidden;
    background: var(--page);
  }
  .sheet {
    position: relative;
    width: 992px;
    height: 1200px;
    font-family: "Montserrat", Arial, sans-serif;
    color: var(--ink);
  }
  .card {
    position: absolute;
    left: 37px;
    width: 930px;
    height: 531px;
    box-sizing: border-box;
    overflow: hidden;
    background: var(--page);
  }
  .card--front { top: 25px; border: 1px solid var(--frame-front); }
  .card--back { top: 645px; border: 1px solid var(--frame-back); }
  .sculpture-photo {
    position: absolute;
    inset: 0;
    width: 100%;
    height: 100%;
  }
  .contact {
    position: absolute;
    left: 443px;
    top: 228px;
  }
  .contact__business {
    margin: 0 0 17px;
    font-weight: 700;
    font-size: 23px;
    letter-spacing: 0.2px;
    line-height: 24px;
    text-transform: uppercase;
  }
  .contact__line {
    margin: 0;
    font-weight: 400;
    font-size: 20px;
    line-height: 26.5px;
    letter-spacing: 0.3px;
    text-transform: uppercase;
  }
  .notes-label {
    position: absolute;
    left: 32px;
    top: 444px;
    margin: 0;
    font-weight: 700;
    font-size: 27px;
    line-height: 32px;
    letter-spacing: 0.2px;
    text-transform: uppercase;
  }
  .writing-lines {
    position: absolute;
    left: 32px;
    top: 486px;
    width: 480px;
    height: 1px;
    background: var(--rule);
  }
</style>
</head>
<body>
<div class="sheet">

  <section class="card card--front">
    <svg class="sculpture-photo" viewBox="0 0 930 531" preserveAspectRatio="none" role="img" aria-label="Photograph of a polished agate slice sculpture with banded brown and grey stone">
      <defs>
        <linearGradient id="stoneFront" x1="0" y1="0" x2="1" y2="1">
          <stop offset="0" stop-color="var(--stone-dark)"/>
          <stop offset="0.55" stop-color="var(--stone-mid)"/>
          <stop offset="0.8" stop-color="var(--stone-light)"/>
          <stop offset="1" stop-color="var(--stone-dark)"/>
        </linearGradient>
      </defs>
      <path d="M0,170 C60,130 110,90 150,100 C230,150 330,200 400,230 C400,300 410,360 470,400 C580,460 760,480 860,531 L0,531 Z"
            fill="url(#stoneFront)"/>
    </svg>
    <div class="contact">
      <h1 class="contact__business">Fernvale Craft Works</h1>
      <p class="contact__line">Marlo Prewitt</p>
      <p class="contact__line">555.213.4098</p>
      <p class="contact__line">marlo@quillbrookmail.com</p>
    </div>
  </section>

  <section class="card card--back">
    <svg class="sculpture-photo" viewBox="0 0 930 531" preserveAspectRatio="none" role="img" aria-label="Faded photograph of the agate slice sculpture sweeping across the card">
      <defs>
        <linearGradient id="stoneBack" x1="0" y1="0" x2="1" y2="1">
          <stop offset="0" stop-color="var(--stone-pale-b)"/>
          <stop offset="0.5" stop-color="var(--stone-pale-a)"/>
          <stop offset="1" stop-color="var(--stone-pale-b)"/>
        </linearGradient>
      </defs>
      <path d="M0,0 L570,0 C580,70 600,130 680,170 C760,210 860,240 930,260 L930,531 C760,520 520,500 350,440 C200,380 80,280 0,190 Z"
            fill="url(#stoneBack)"/>
    </svg>
    <h2 class="notes-label">Notes</h2>
    <div class="writing-lines"></div>
  </section>

</div>
</body>
</html>
```